Kalewero Tea & Dairy Farm Website

Design a mainly visual informational website incorporating examples uploaded of a tea and dairy farm in Africa. I can provide more pictures.

I do take suggestions willing.

Industry/Entity Type

Farm

Font styles to use
Serif

Colors
acd037

```html
<!DOCTYPE html>
<html lang="en">
<head>
<meta charset="utf-8">
<title>Kalewero Tea &amp; Dairy Farm</title>
<link href="https://fonts.googleapis.com/css2?family=Open+Sans:wght@400;600;700&display=swap" rel="stylesheet">
<style>
:root{
  --green:#8cc63f;
  --green-text:#5fa21c;
  --footer-green:#4dab2e;
  --dark:#333;
  --mid:#555;
  --grey:#888;
  --light:#f2f2f2;
  --line:#dcdcdc;
  --blue:#4a8fd6;
  --bar:#232323;
}
*{margin:0;padding:0;box-sizing:border-box}
html,body{width:920px;height:1200px;overflow:hidden;background:#fff}
body{font-family:"Open Sans",sans-serif;color:var(--dark);position:relative}
.abs{position:absolute}

.topbar{left:0;top:0;width:920px;height:54px;background:var(--green)}
.topbar-rule{left:0;top:54px;width:920px;height:4px;background:#555}
.brand{left:77px;top:8px;font-size:24px;font-weight:700;color:#fff;letter-spacing:.2px}
.search{left:566px;top:14px;width:152px;height:24px;background:#fff;border-radius:2px;font-size:10px;color:#999;padding:5px 9px}
.search svg{position:absolute;right:5px;top:4px}
.search-sep{position:absolute;right:24px;top:3px;width:1px;height:18px;background:#ccc}
.btn{top:14px;height:24px;font-size:10px;color:#fff;border-radius:2px;text-align:center;line-height:24px;font-weight:600}
.btn-register{left:723px;width:63px;background:var(--blue)}
.btn-login{left:792px;width:50px;background:#333}

.nav-mark{left:114px;top:58px;width:0;height:0;border-left:6px solid transparent;border-right:6px solid transparent;border-top:7px solid #555}
.nav{top:75px;font-size:11px;color:#888;letter-spacing:.2px}
.nav.active{color:#222;font-weight:600}

.hero{left:0;top:104px;width:920px;height:334px;background:linear-gradient(180deg,#b9d4ea 0%,#d7e6ef 22%,#6f9a4a 34%,#7fae3e 55%,#8bbf3c 100%)}
.hero-arrow{top:247px;width:38px;height:48px;background:rgba(30,40,20,.55)}
.hero-caption{left:77px;top:328px;width:359px;height:33px;background:rgba(35,35,20,.85);color:#fff;font-size:18px;line-height:33px;padding-left:8px}
.hero-more{left:77px;top:364px;width:100px;height:34px;background:rgba(230,240,210,.85);font-size:14px;line-height:34px;text-align:center;color:#222}

.intro{left:112px;top:465px;width:696px;text-align:center;font-size:12px;line-height:19.2px;color:#666}
.rule{left:77px;width:767px;height:1px;background:var(--line)}

.card-img{top:588px;width:182px;height:102px}
.card-title{top:694px;width:190px;text-align:center;font-size:13px;line-height:18px;color:var(--green-text)}

.section-title{top:774px;font-size:18px;color:#222}
.news-thumb{top:808px;width:53px;height:42px}
.news-date{top:815px;font-size:8px;color:#999}
.news-head{top:824px;font-size:10px;line-height:12px;color:#222}
.news-body{top:858px;width:165px;font-size:9.5px;line-height:16px;color:#999}
.video{left:661px;top:808px;width:182px;height:111px;background:linear-gradient(180deg,#9fb0a8 0%,#7a8a6a 45%,#5b7a35 100%)}
.play{left:731px;top:849px;width:41px;height:28px;background:#111;border-radius:5px}

.footer{left:0;top:958px;width:920px;height:196px;background:var(--light)}
.foot-head{top:982px;font-size:12px;color:var(--footer-green)}
.foot-link{font-size:9.5px;color:#555}
.social{top:1106px;width:22px;height:22px;border:1px solid #ccc;border-radius:3px;background:#fff}
.field{left:596px;width:177px;border:1px solid #ddd;background:#fff;border-radius:2px;font-size:9.5px;color:#555;padding:8px 9px}
.submit{left:779px;top:1105px;width:49px;height:23px;background:#555;color:#eee;font-size:9.5px;line-height:23px;text-align:center;border-radius:2px}

.bottom{left:0;top:1154px;width:920px;height:46px;background:var(--bar);color:#aaa;font-size:9.5px;text-align:center;line-height:46px}
</style>
</head>
<body>

<header>
  <div class="abs topbar"></div>
  <div class="abs topbar-rule"></div>
  <div class="abs brand">Kalewero Tea &amp; Dairy Farm</div>
  <div class="abs search">Search<span class="search-sep"></span>
    <svg width="14" height="14" viewBox="0 0 14 14"><circle cx="5.5" cy="5.5" r="4.3" fill="none" stroke="#888" stroke-width="1.6"/><line x1="8.6" y1="8.6" x2="13" y2="13" stroke="#888" stroke-width="1.8"/></svg>
  </div>
  <div class="abs btn btn-register">REGISTER</div>
  <div class="abs btn btn-login">LOG IN</div>

  <div class="abs nav-mark"></div>
  <nav>
    <span class="abs nav active" style="left:104px">HOME</span>
    <span class="abs nav" style="left:173px">ABOUT US</span>
    <span class="abs nav" style="left:263px">SERVICES</span>
    <span class="abs nav" style="left:348px">PRODUCTS</span>
    <span class="abs nav" style="left:442px">NEWS AND EVENTS</span>
    <span class="abs nav" style="left:579px">PARTNERS</span>
    <span class="abs nav" style="left:670px">CAREER</span>
    <span class="abs nav" style="left:746px">CONTACT US</span>
  </nav>
</header>

<section class="hero-slider">
  <div class="abs hero" role="img" aria-label="Black and white dairy cow standing in a green pasture under a blue sky"></div>
  <div class="abs hero-arrow" style="left:0">
    <svg width="38" height="48" viewBox="0 0 38 48"><polyline points="23,12 11,24 23,36" fill="none" stroke="#fff" stroke-width="1.5"/></svg>
  </div>
  <div class="abs hero-arrow" style="left:882px">
    <svg width="38" height="48" viewBox="0 0 38 48"><polyline points="15,12 27,24 15,36" fill="none" stroke="#fff" stroke-width="1.5"/></svg>
  </div>
  <div class="abs hero-caption">Vivamus eu erat at leo ultrices pharetrsa</div>
  <div class="abs hero-more">READ MORE</div>
</section>

<p class="abs intro">Cras turpis arcu, faucibus vel tristique eget, tincidunt at diam. Donec ut dignissim dolor, at dapibus velit. Vestibulum, risus a vulputate gravida, neque libero posuere leo, a interdum ipsum eros id lacus. Phasellus sollicitudin sapien sed quam blandit, sit amet fringilla neque sagittis. Morbi eget placerat mi. Mauris pellentesque, dui at ornare ornare, nisi leo tincidunt magna, in feugiat orci arcu sed nunc. Nulla posuere non nunc a scelerisque.</p>

<div class="abs rule" style="top:568px"></div>

<section class="services">
  <div class="abs card-img" style="left:78px;background:linear-gradient(180deg,#6b6d70,#3a3a38 55%,#7a5a35)" role="img" aria-label="Dairy cows feeding at a barn stall"></div>
  <div class="abs card-title" style="left:74px">Animal Feeding Solutions</div>
  <div class="abs card-img" style="left:272px;background:linear-gradient(135deg,#e8e2d8,#b7a58c 60%,#9d8a6a)" role="img" aria-label="Child feeding a goat"></div>
  <div class="abs card-title" style="left:268px">Locally Adopted Animal Feeding Solutions</div>
  <div class="abs card-img" style="left:466px;background:linear-gradient(180deg,#5a4a4e,#6a9a3a 50%,#4f8a2a)" role="img" aria-label="Rows of hydroponic lettuce seedlings"></div>
  <div class="abs card-title" style="left:462px">Organic Nursery &amp; Hydroponic Farming</div>
  <div class="abs card-img" style="left:661px;background:linear-gradient(135deg,#c87aa0,#7ea850 55%,#5d8c35)" role="img" aria-label="Farm workers harvesting leafy vegetables"></div>
  <div class="abs card-title" style="left:657px">Sustainable Dairy Farming in Practice</div>
</section>

<div class="abs rule" style="top:752px"></div>

<section class="news">
  <h2 class="abs section-title" style="left:77px;font-weight:400">Latest News &amp; Events</h2>
  <svg class="abs" style="left:634px;top:779px" width="15" height="15" viewBox="0 0 15 15"><circle cx="7.5" cy="7.5" r="6.5" fill="none" stroke="#555" stroke-width="1.2"/><path d="M4.5 7.5h5.5M7.8 5l2.4 2.5-2.4 2.5" fill="none" stroke="#555" stroke-width="1.2"/></svg>

  <div class="abs news-thumb" style="left:78px;background:linear-gradient(135deg,#c96a4a,#8a9ab8)" role="img" aria-label="Colourful town buildings"></div>
  <div class="abs news-date" style="left:140px">Jun 20, 2014</div>
  <div class="abs news-head" style="left:139px">Phasellus eu enim id<br>felis feugiat rutrum</div>
  <p class="abs news-body" style="left:78px">Nam semper facilisis enim id fringilla. Vestibulum ante ipsum primis in faucibus orci luctus et ultrices posu ere cubilia Curae;</p>

  <div class="abs news-thumb" style="left:274px;background:linear-gradient(135deg,#8fae6a,#d8b8a0)" role="img" aria-label="Couple sharing a picnic meal"></div>
  <div class="abs news-date" style="left:336px">Jun 20, 2014</div>
  <div class="abs news-head" style="left:334px">Phasellus eu enim id<br>felis feugiat rutrum</div>
  <p class="abs news-body" style="left:274px">Nam semper facilisis enim id fring-illa. Vestibulum ante ipsum primis in faucibus orci luctus et ultrices posu ere cubilia Curae;</p>

  <div class="abs news-thumb" style="left:468px;background:linear-gradient(135deg,#f2f2ea,#6fae3a 50%,#c09060)" role="img" aria-label="Fresh green beans on a board"></div>
  <div class="abs news-date" style="left:530px">Jun 20, 2014</div>
  <div class="abs news-head" style="left:529px">Phasellus eu enim id<br>felis feugiat rutrum</div>
  <p class="abs news-body" style="left:468px">Nam semper facilisis enim id fring-illa. Vestibulum ante ipsum primis in faucibus orci luctus et ultrices posu ere cubilia Curae;</p>

  <h2 class="abs section-title" style="left:661px;font-weight:400">What we do</h2>
  <div class="abs video" role="img" aria-label="Video still of a farmer crouching beside grazing cows"></div>
  <div class="abs play"><svg width="41" height="28" viewBox="0 0 41 28"><polygon points="15,6 29,14 15,22" fill="#fff"/></svg></div>
</section>

<footer>
  <div class="abs footer"></div>
  <h3 class="abs foot-head" style="left:93px;font-weight:400">Navigation Menu</h3>
  <span class="abs foot-link" style="left:93px;top:1009px">Home</span>
  <span class="abs foot-link" style="left:93px;top:1028px">About us</span>
  <span class="abs foot-link" style="left:93px;top:1047px">Services</span>
  <span class="abs foot-link" style="left:93px;top:1067px">Products</span>
  <span class="abs foot-link" style="left:174px;top:1009px">News and Events</span>
  <span class="abs foot-link" style="left:174px;top:1028px">Partners</span>
  <span class="abs foot-link" style="left:174px;top:1047px">Career</span>
  <span class="abs foot-link" style="left:174px;top:1067px">Contact us</span>

  <div class="abs social" style="left:94px"></div>
  <div class="abs social" style="left:120px"></div>
  <div class="abs social" style="left:146px"></div>
  <div class="abs social" style="left:172px"><svg width="20" height="20" viewBox="0 0 20 20"><rect x="5" y="6.5" width="10" height="7" fill="none" stroke="#777" stroke-width="1.2"/><polyline points="5,6.5 10,10.5 15,6.5" fill="none" stroke="#777" stroke-width="1.2"/></svg></div>
  <div class="abs social" style="left:198px"><svg width="20" height="20" viewBox="0 0 20 20"><circle cx="6.5" cy="13.5" r="1.3" fill="#777"/><path d="M5.5 9a5.5 5.5 0 0 1 5.5 5.5M5.5 5.5a9 9 0 0 1 9 9" fill="none" stroke="#777" stroke-width="1.4"/></svg></div>

  <h3 class="abs foot-head" style="left:293px;font-weight:400">Support Links</h3>
  <span class="abs foot-link" style="left:293px;top:1009px">Privacy Policy</span>
  <span class="abs foot-link" style="left:293px;top:1028px">Terms and Conditions</span>
  <span class="abs foot-link" style="left:293px;top:1047px">Customer Support</span>
  <span class="abs foot-link" style="left:293px;top:1067px">FAQ</span>

  <h3 class="abs foot-head" style="left:446px;font-weight:400">Contact us</h3>
  <span class="abs foot-link" style="left:446px;top:1009px;line-height:14.5px">55 Building name,<br>Street name<br>City - Zip code</span>
  <svg class="abs" style="left:446px;top:1062px" width="21" height="21" viewBox="0 0 21 21"><rect x="1" y="4" width="19" height="16" fill="#444"/><rect x="4" y="1" width="3" height="5" fill="#444"/><rect x="14" y="1" width="3" height="5" fill="#444"/><rect x="4" y="8" width="13" height="3" fill="#fff"/><rect x="9" y="13" width="3" height="7" fill="#fff"/></svg>
  <span class="abs foot-link" style="left:474px;top:1067px">Get Directions</span>

  <h3 class="abs foot-head" style="left:598px;font-weight:400">Contact us</h3>
  <div class="abs field" style="top:1014px;height:27px">Name</div>
  <div class="abs field" style="top:1046px;height:27px">E-mail</div>
  <div class="abs field" style="top:1078px;height:51px">Comment</div>
  <div class="abs submit">SUBMIT</div>

  <div class="abs bottom">Copyright &copy; 2014 Kalewero Tea &amp; Dairy Farm. &nbsp;All rights reserved.</div>
</footer>

</body>
</html>
```